Fahrzeugbeschriftung für Dienstleister in den Bereichen Sicherheitstechnik und Elektrotechnik
Zielgruppe
Guten Tag, wir beschäftigen uns mit der Sicherheitstechnik und Elektrotechnik! Siehe www.tl-schutztechnik.de!
Nun erweitern wir unseren Bereich um Fenster und Türen. Dafür bekommt unser Mitarbeiter einen Velmar Kargo Plus Line L2. Nun wollen wir ihn nicht wie unsere anderen Fahrzeuge einfach bekleben!
Wie unsere jetzige Fahrzeuge beschriftet sind, können Sie im Anhang sehen!
Gruß TL Schutztechnik

```html
<!DOCTYPE html>
<html lang="de">
<head>
<meta charset="utf-8">
<title>TL Schutztechnik – Fahrzeugbeschriftung</title>
<link href="https://fonts.googleapis.com/css2?family=Open+Sans:wght@600;700;800&family=Oswald:wght@500&display=swap" rel="stylesheet">
<style>
  :root{
    --bg:#e3e4e8;
    --bg-alt:#dcdde2;
    --navy:#1b4f8a;
    --navy-deep:#163f70;
    --red:#c8202f;
    --white:#ffffff;
    --body-line:#c9ccd3;
    --skirt:#2b2d31;
    --glass:#4a4d54;
  }
  html,body{margin:0;padding:0;overflow:hidden;background:var(--bg);}
  .canvas{width:720px;height:1200px;display:block;}
  .band-alt{fill:var(--bg-alt);}
  .body{fill:var(--white);stroke:var(--body-line);stroke-width:1;}
  .skirt{fill:var(--skirt);}
  .glass{fill:var(--glass);}
  .blue{fill:var(--navy);}
  .blue-deep{fill:var(--navy-deep);}
  .url-strip{fill:var(--white);}
  .brand-disc{fill:var(--white);}
  .brand-name{font-family:"Open Sans",sans-serif;font-weight:700;fill:var(--navy);text-anchor:middle;font-size:14px;}
  .services{font-family:"Oswald",sans-serif;font-weight:500;fill:var(--navy);font-size:11px;}
  .headline{font-family:"Open Sans",sans-serif;font-weight:800;fill:var(--navy);font-size:16px;}
  .pill{fill:var(--red);}
  .pill-text{font-family:"Oswald",sans-serif;font-weight:500;fill:var(--white);font-size:15px;text-anchor:middle;}
  .claim{font-family:"Open Sans",sans-serif;font-weight:700;fill:var(--red);font-size:10px;}
  .address{font-family:"Open Sans",sans-serif;font-weight:700;fill:var(--white);font-size:11px;}
  .phone{font-family:"Open Sans",sans-serif;font-weight:800;fill:var(--white);font-size:12px;}
  .url{font-family:"Open Sans",sans-serif;font-weight:700;fill:var(--navy-deep);font-size:13px;letter-spacing:3px;text-anchor:middle;}
  .grille{fill:#d9dbe0;stroke:#9ea2aa;stroke-width:1;}
  .lamp{fill:#b8242f;}
  .door-seam{stroke:var(--body-line);stroke-width:1;}

  .rear .headline{font-size:11px;text-anchor:middle;}
  .rear .pill-text{font-size:10px;}
  .rear .services{font-size:7px;text-anchor:middle;}
  .rear .brand-name{font-size:9px;}
  .rear .claim{font-size:9px;text-anchor:middle;}
  .rear .address{font-size:9px;}
  .rear .phone{font-size:10px;}
  .front .brand-name{font-size:8px;}
</style>
</head>
<body>
<svg class="canvas" viewBox="0 0 720 1200" xmlns="http://www.w3.org/2000/svg">
  <defs>
    <g id="side-shapes">
      <path class="body" d="M10,245 L10,70 Q12,30 50,26 L420,22 Q450,22 480,40 L600,130 Q655,150 668,195 L670,245 Z"/>
      <path class="blue-deep" d="M85,24 L280,24 L330,100 L300,128 Z"/>
      <path class="blue" d="M330,118 L470,140 L600,142 L650,180 L668,205 L668,215 L390,215 L335,200 Z"/>
      <path class="glass" d="M455,45 Q470,42 480,48 L575,128 L455,128 Z"/>
      <rect class="skirt" x="10" y="215" width="660" height="35" rx="4"/>
      <rect class="url-strip" x="205" y="226" width="270" height="18" rx="2"/>
      <circle class="brand-disc" cx="340" cy="140" r="72"/>
    </g>
  </defs>

  <!-- Seitenansicht Beifahrerseite -->
  <g class="side side-passenger" transform="translate(20,40)">
    <use href="#side-shapes"/>
    <text class="brand-name" x="340" y="138">TL Schutztechnik</text>
    <text class="brand-name" x="340" y="158">GmbH</text>
    <text class="services" text-anchor="end">
      <tspan x="178" y="82">ELEKTROTECHNIK</tspan>
      <tspan x="178" y="96">FENSTER- UND TÜRSICHERUNG</tspan>
      <tspan x="178" y="110">FUNK-ALARMANLAGEN</tspan>
      <tspan x="178" y="124">EINBRUCHMELDEANLAGEN</tspan>
      <tspan x="178" y="138">BRANDMELDEANLAGEN</tspan>
      <tspan x="178" y="152">VIDEOÜBERWACHUNG</tspan>
    </text>
    <text class="headline" x="66" y="180">JETZT NEU</text>
    <rect class="pill" x="166" y="162" width="140" height="24" rx="6"/>
    <text class="pill-text" x="236" y="180" textLength="124" lengthAdjust="spacingAndGlyphs">FENSTER UND TÜREN</text>
    <text class="claim" x="186" y="203">Meisterbetrieb mit Zertifizierung</text>
    <text class="address" text-anchor="end"><tspan x="562" y="170">Lindenweg 14</tspan><tspan x="562" y="184">58210 Halvern</tspan></text>
    <text class="phone" x="562" y="204" text-anchor="end">Tel.: 0 23 45 / 61 09 284</text>
    <text class="url" x="340" y="240">tl-schutztechnik.de</text>
  </g>

  <rect class="band-alt" x="0" y="380" width="720" height="380"/>

  <!-- Seitenansicht Fahrerseite -->
  <g class="side side-driver">
    <use href="#side-shapes" transform="translate(700,430) scale(-1,1)"/>
    <g transform="translate(20,430)">
      <text class="brand-name" x="360" y="138">TL Schutztechnik</text>
      <text class="brand-name" x="360" y="158">GmbH</text>
      <text class="services">
        <tspan x="502" y="84">ELEKTROTECHNIK</tspan>
        <tspan x="502" y="98">FENSTER- UND TÜRSICHERUNG</tspan>
        <tspan x="502" y="112">FUNK-ALARMANLAGEN</tspan>
        <tspan x="502" y="126">EINBRUCHMELDEANLAGEN</tspan>
        <tspan x="502" y="140">BRANDMELDEANLAGEN</tspan>
        <tspan x="502" y="154">VIDEOÜBERWACHUNG</tspan>
      </text>
      <text class="headline" x="400" y="154">JETZT NEU</text>
      <rect class="pill" x="394" y="162" width="140" height="24" rx="6"/>
      <text class="pill-text" x="464" y="180" textLength="124" lengthAdjust="spacingAndGlyphs">FENSTER UND TÜREN</text>
      <text class="claim"><tspan x="400" y="199">Meisterbetrieb mit</tspan><tspan x="400" y="211">Zertifizierung</tspan></text>
      <text class="address"><tspan x="140" y="170">Lindenweg 14</tspan><tspan x="140" y="184">58210 Halvern</tspan></text>
      <text class="phone" x="140" y="204">Tel.: 0 23 45 / 61 09 284</text>
      <text class="url" x="360" y="240">tl-schutztechnik.de</text>
    </g>
  </g>

  <!-- Heckansicht -->
  <g class="rear">
    <rect class="body" x="110" y="820" width="230" height="300" rx="22"/>
    <rect class="lamp" x="112" y="950" width="12" height="80" rx="3"/>
    <rect class="lamp" x="326" y="950" width="12" height="80" rx="3"/>
    <rect class="blue" x="124" y="1035" width="202" height="45"/>
    <rect class="skirt" x="118" y="1080" width="214" height="38" rx="6"/>
    <line class="door-seam" x1="225" y1="830" x2="225" y2="1118"/>
    <text class="headline" x="172" y="876">JETZT NEU</text>
    <rect class="pill" x="128" y="884" width="88" height="17" rx="4"/>
    <text class="pill-text" x="172" y="896.5" textLength="80" lengthAdjust="spacingAndGlyphs">FENSTER UND TÜREN</text>
    <text class="services">
      <tspan x="172" y="916">ELEKTROTECHNIK</tspan>
      <tspan x="172" y="925">FENSTER- UND TÜRSICHERUNG</tspan>
      <tspan x="172" y="934">FUNK-ALARMANLAGEN</tspan>
      <tspan x="172" y="943">EINBRUCHMELDEANLAGEN</tspan>
      <tspan x="172" y="952">BRANDMELDEANLAGEN</tspan>
      <tspan x="172" y="961">VIDEOÜBERWACHUNG</tspan>
    </text>
    <text class="brand-name" x="279" y="912">TL Schutztechnik</text>
    <text class="brand-name" x="279" y="924">GmbH</text>
    <text class="claim" x="225" y="996">Meisterbetrieb mit Zertifizierung</text>
    <text class="address" x="140" y="1053">Lindenweg 14 58210 Halvern</text>
    <text class="phone" x="140" y="1068">Tel.: 0 23 45 / 61 09 284</text>
  </g>

  <!-- Frontansicht -->
  <g class="front">
    <rect class="body" x="400" y="820" width="250" height="300" rx="22"/>
    <rect class="glass" x="418" y="865" width="214" height="80" rx="8"/>
    <rect class="blue" x="404" y="990" width="242" height="60" rx="10"/>
    <rect class="grille" x="465" y="995" width="120" height="45" rx="10"/>
    <rect class="skirt" x="408" y="1050" width="234" height="60" rx="8"/>
    <circle cx="525" cy="965" r="4" fill="var(--navy)"/>
    <text class="brand-name" x="525" y="981">TL Schutztechnik</text>
  </g>
</svg>
</body>
</html>
```